Letter design, envelope design, and more

Hello, we the Varlo Gmbh are looking for our shop. Letter C5. Design does not have to be like a business card, so it can have straight lines. Only the color is important. The logo is the text under VaRLo omit.It should not be playful but Profesionel

Font styles to use
Sans Serif

Colors
0555a3
3176b5
85abd2
85cae6
34a7d8
0792cd
cee9f5
cfdfed
000000

Requirements
Must have
• Color like business card, Please, with the text under VaRLo, Correct address Benkelstr. 4 Zip code 9512 Goldach, as well as Couvert Without addressing only design and logo with VaRlo
Nice to have
• more writing articles
Should not have
• Not too colored, Text under VaRLo, bright colors

```html
<!DOCTYPE html>
<html lang="de">
<head>
<meta charset="utf-8">
<title>VaRLo Gmbh – Geschäftsausstattung</title>
<link rel="stylesheet" href="https://fonts.googleapis.com/css2?family=Roboto:wght@400;500;700&display=swap">
<style>
  :root{
    --navy:#0b1f56;
    --grey-line:#8c8f9c;
    --paper:#f4f4f4;
    --backdrop:#d2d2d2;
    --text:#4a4a4a;
    --rule-light:#c9c9c9;
  }
  *{margin:0;padding:0;box-sizing:border-box}
  html,body{width:1200px;height:810px;overflow:hidden}
  body{background:var(--backdrop);font-family:"Roboto",sans-serif;color:var(--text)}
  .stage{position:relative;width:1200px;height:810px}

  .sheet{position:absolute;background:var(--paper);overflow:hidden}

  /* wordmark */
  .wordmark{display:flex;align-items:center;gap:6px;color:var(--navy);font-weight:700;letter-spacing:.5px;white-space:nowrap}
  .wordmark .dot{background:var(--navy);display:block}
  .wordmark--lg{font-size:25px}
  .wordmark--lg .dot{width:30px;height:30px}

  /* contact block */
  .contact{font-size:7.4px;line-height:10.2px;color:var(--text)}
  .contact .address{margin-bottom:3px}
  .contact .row{display:flex;align-items:center;gap:4px}
  .contact svg{width:8px;height:8px;fill:var(--navy);flex:none}

  /* letterhead */
  .letterhead{left:137px;top:110px;width:436px;height:614px}
  .letterhead .wordmark{position:absolute;left:35px;top:52px}
  .letterhead .contact{position:absolute;left:340px;top:40px}
  .letterhead .rule-accent{position:absolute;left:35px;top:116px;width:135px;height:3px;background:var(--navy)}
  .letterhead .rule-base{position:absolute;left:172px;top:117px;width:371px;height:1px;background:var(--rule-light)}
  .footer-stripe{position:absolute;left:0;right:0;height:3px;background:var(--grey-line)}
  .footer-band{position:absolute;left:0;right:0;bottom:0;background:var(--navy)}
  .letterhead .footer-stripe{bottom:18px}
  .letterhead .footer-band{height:16px}

  /* envelope back */
  .envelope-back{left:619px;top:193px;width:444px;height:222px;background:var(--paper)}
  .envelope-back .flap{position:absolute;left:0;top:0;width:444px;height:66px}
  .envelope-back .flap-name{position:absolute;left:0;right:0;top:16px;text-align:center;color:#fff;font-weight:700;font-size:22px;letter-spacing:.5px}

  /* envelope front */
  .envelope-front{left:618px;top:444px;width:445px;height:221px}
  .envelope-front .wordmark{position:absolute;left:30px;top:26px}
  .envelope-front .contact{position:absolute;left:31px;top:80px}
  .envelope-front .footer-stripe{bottom:18px}
  .envelope-front .footer-band{height:16px}
</style>
</head>
<body>
<main class="stage">

  <section class="sheet letterhead" aria-label="Briefbogen">
    <div class="wordmark wordmark--lg"><span class="dot"></span>VaRLo Gmbh</div>
    <address class="contact">
      <div class="address">Benkelstr. 4<br>9512 Goldach</div>
      <div class="row"><svg viewBox="0 0 10 10"><path d="M2 0.5l2 2.3-1 1.2c.6 1.3 1.7 2.4 3 3l1.2-1 2.3 2-1.1 1.5C4.6 9.2.8 5.4.5 1.6z"/></svg>+41 71 555 04 20</div>
      <div class="row"><svg viewBox="0 0 10 10"><path d="M0 2h10v6H0z"/><path d="M0 2l5 3.5L10 2" fill="none" stroke="#f4f4f4" stroke-width="1"/></svg>info@varlo.ch</div>
      <div class="row"><svg viewBox="0 0 10 10"><circle cx="5" cy="5" r="4.5"/><path d="M.5 5h9M5 .5c-2 2.5-2 6.5 0 9M5 .5c2 2.5 2 6.5 0 9" fill="none" stroke="#f4f4f4" stroke-width=".7"/></svg>www.varlo.ch</div>
    </address>
    <div class="rule-base"></div>
    <div class="rule-accent"></div>
    <div class="footer-stripe"></div>
    <div class="footer-band"></div>
  </section>

  <section class="sheet envelope-back" aria-label="Couvert Rückseite">
    <svg class="flap" viewBox="0 0 444 66" aria-hidden="true">
      <path d="M0 0H444L436 54Q434 65 422 65H22Q11 65 9 54Z" fill="var(--navy)"/>
    </svg>
    <div class="flap-name">VaRLo</div>
  </section>

  <section class="sheet envelope-front" aria-label="Couvert Vorderseite">
    <div class="wordmark wordmark--lg"><span class="dot"></span>VaRLo Gmbh</div>
    <address class="contact">
      <div class="address">Benkelstr. 4<br>9512 Goldach</div>
      <div class="row"><svg viewBox="0 0 10 10"><path d="M2 0.5l2 2.3-1 1.2c.6 1.3 1.7 2.4 3 3l1.2-1 2.3 2-1.1 1.5C4.6 9.2.8 5.4.5 1.6z"/></svg>+41 71 555 04 20</div>
      <div class="row"><svg viewBox="0 0 10 10"><path d="M0 2h10v6H0z"/><path d="M0 2l5 3.5L10 2" fill="none" stroke="#f4f4f4" stroke-width="1"/></svg>info@varlo.ch</div>
      <div class="row"><svg viewBox="0 0 10 10"><circle cx="5" cy="5" r="4.5"/><path d="M.5 5h9M5 .5c-2 2.5-2 6.5 0 9M5 .5c2 2.5 2 6.5 0 9" fill="none" stroke="#f4f4f4" stroke-width=".7"/></svg>www.varlo.ch</div>
    </address>
    <div class="footer-stripe"></div>
    <div class="footer-band"></div>
  </section>

</main>
</body>
</html>
```